Create a website for a car broker/car buyers advocate

build a website to suit a car brokering/car buying service. The design should communicate saving people time, money and stress by outsourcing the purchasing process for thier new car. I woudl like a modern site which is scroll able all on one page and wouldnt mind a dark or minimalistic theme. i have uploaded the logo which has also been designed by pixel harbor

Target Market(s)

general consumers, new car buyers, car collectors

Industry/Entity Type

Car Dealer

Font styles to use
Sans Serif

Colors

Designer to choose colors to be used in the design.

Requirements
Must have
• single page scrollable site
• modern design
• professional but fun
Nice to have
• some websites i like of similar businesses are :
• http://www.motorvane.com.au/
• https://drivelynx.com.au/

```html
<!DOCTYPE html>
<html lang="en">
<head>
<meta charset="utf-8">
<title>Kestrel Brokers — Car Broker</title>
<link rel="stylesheet" href="https://fonts.googleapis.com/css2?family=Montserrat:wght@400;500;600&display=swap">
<style>
:root{
  --brand:#4f5b7a;
  --brand-dark:#2d3447;
  --brand-soft:#6f7b9a;
  --ink:#2b2b33;
  --muted:#6a6d77;
  --line:#d9dce3;
  --white:#ffffff;
  --bg:#ffffff;
}
*{box-sizing:border-box;margin:0;padding:0}
html,body{width:1200px;height:3875px;overflow:hidden}
body{position:relative;background:var(--bg);font-family:'Montserrat',sans-serif;color:var(--ink);font-size:14px}
.abs{position:absolute}
.btn{position:absolute;background:var(--brand);color:var(--white);display:flex;align-items:center;justify-content:center;font-size:16px}
.heading{position:absolute;left:0;width:1200px;text-align:center;color:var(--brand);font-size:22px;font-weight:500;letter-spacing:.2px}
.topbar{top:0;left:0;width:1200px;height:38px;background:var(--brand)}
.topbar .phone{left:135px;top:9px;color:var(--white);font-size:16px;display:flex;align-items:center;gap:8px}
.social{position:absolute;width:30px;height:30px;background:var(--brand-soft)}
.sell{left:915px;top:0;width:152px;height:38px;background:var(--brand-soft);color:var(--white);font-size:13px;display:flex;align-items:center;justify-content:center;gap:6px}
.logo{display:flex;align-items:center;gap:10px;color:var(--brand-dark);font-weight:600;letter-spacing:3px;font-size:17px}
.logo .mark{width:18px;height:18px;background:var(--brand-dark)}
.nav{top:90px;left:580px;display:flex;font-size:14px;color:var(--ink)}
.nav span{padding:0 14px;border-right:1px solid #999;line-height:14px}
.nav span:last-child{border:0}
.nav .on{color:var(--brand)}
.hero{top:126px;left:0;width:1200px;height:432px;background:linear-gradient(180deg,#5f6a72 0%,#8b949a 40%,#4c524f 75%,#3a3d3b 100%)}
.hero h1{position:absolute;top:50px;width:1200px;text-align:center;color:var(--white);font-weight:500;font-size:46px;line-height:52px}
.search{top:448px;left:132px;width:936px;height:330px;background:var(--white);box-shadow:0 2px 6px rgba(0,0,0,.25)}
.search .bar{height:47px;background:var(--brand);color:var(--white);font-size:15px;padding:15px 22px}
.tabs{position:absolute;right:22px;top:6px;display:flex;border:1px solid #8b94ad}
.tabs span{width:78px;height:34px;display:flex;align-items:center;justify-content:center;font-size:12px;color:var(--white)}
.tabs .on{background:var(--brand-dark)}
.label{position:absolute;color:var(--brand);font-size:15px;font-weight:500}
.select{position:absolute;top:128px;width:204px;height:36px;border:1px solid #9aa0ad;font-size:13px;color:var(--muted);padding:10px 14px}
.select:after{content:"";position:absolute;right:22px;top:13px;width:5px;height:5px;border-right:1.5px solid #444;border-bottom:1.5px solid #444;transform:rotate(45deg)}
.types{position:absolute;top:244px;left:0;width:936px;display:flex}
.type{position:absolute;text-align:center;font-size:11px;width:110px}
.type svg{display:block;margin:0 auto 6px}
.photo{position:absolute}
.about-photo{top:975px;left:132px;width:441px;height:425px;border:4px solid #8592b4;background:linear-gradient(160deg,#6d8b4a,#a7b78a 45%,#7e8fb3 70%,#3f4a66)}
.about-text{top:975px;left:595px;width:470px;font-size:14px;line-height:29px;color:#333}
.about-text h3{font-weight:500;font-size:19px;margin:6px 0 8px;color:#222}
.about-text li{list-style:none;display:flex;align-items:center;gap:14px;margin-bottom:9px}
.brands{top:1620px;left:132px;width:201px}
.brands div{height:43px;border-bottom:1px solid #e4e6ea;display:flex;align-items:center;padding-left:22px;font-size:13px;position:relative}
.brands div:before{content:"";position:absolute;left:5px;top:14px;width:3px;height:15px;background:var(--brand)}
.brands .on{color:var(--brand)}
.card{position:absolute;top:1610px;width:230px;height:262px;background:var(--white);box-shadow:0 1px 5px rgba(0,0,0,.18);text-align:center}
.card .img{height:118px}
.card h4{color:var(--brand);font-weight:500;font-size:15px;margin-top:13px}
.card p{font-size:14px;color:#333;margin-top:3px}
.price{display:flex;justify-content:center;gap:8px;margin-top:10px}
.price span{background:var(--brand-soft);color:var(--white);font-size:14px;padding:4px 8px}
.price i{width:26px;height:26px;background:var(--brand-soft);display:flex;align-items:center;justify-content:center}
.card .get{display:inline-block;margin-top:12px;background:var(--brand-dark);color:var(--white);font-size:14px;padding:5px 9px}
.band{top:1968px;left:0;width:1200px;height:209px;background:var(--brand)}
.quote{position:absolute;top:2125px;width:301px;height:187px;background:var(--white);box-shadow:0 1px 5px rgba(0,0,0,.2)}
.quote h5{color:var(--brand-dark);font-weight:500;font-size:15px;margin:18px 0 0 20px}
.quote h5 b{color:#bbb;font-weight:600;margin-right:4px}
.quote p{font-size:12.5px;line-height:20px;margin:10px 20px 0 20px;color:#333}
.quote .name{position:absolute;left:0;top:132px;width:144px;height:27px;background:var(--brand-soft);color:var(--white);font-size:15px;padding:4px 24px;border-radius:0 14px 14px 0}
.quote .stars{position:absolute;right:26px;top:136px;color:#bbb;font-size:14px;letter-spacing:5px}
.arrow{position:absolute;top:2192px}
.products p{position:absolute;top:2483px;left:210px;width:780px;text-align:center;font-size:14px;line-height:28px;color:#333}
.prod{position:absolute;top:2568px;width:150px;text-align:center;font-size:16px;line-height:24px;color:#222}
.prod .box{width:135px;height:122px;margin:0 auto 16px;border:3px solid #e5e7ec;transform:skewX(-10deg);display:flex;align-items:center;justify-content:center}
.prod .box svg{transform:skewX(10deg)}
.faq{position:absolute;left:216px;width:768px;border:1px solid #c9ccd3;font-size:14px;padding:10px 13px;color:#222}
.faq svg{position:absolute;right:18px;top:13px}
.faq p{font-size:13px;line-height:22px;color:#444;margin-top:16px;width:690px}
.footer{top:3473px;left:0;width:1200px;height:402px;background:linear-gradient(180deg,#4c5878 0%,#56607f 55%,#3f4a66 100%)}
.fnav{top:3700px;left:0;width:1200px;display:flex;justify-content:center;color:var(--white);font-size:14px}
.fnav span{padding:0 20px;border-right:1px solid #ddd;line-height:14px}
.fnav span:last-child{border:0}
.copy{top:3840px;width:1200px;text-align:center;color:var(--white);font-size:12px}
</style>
</head>
<body>

<header class="abs topbar">
  <div class="abs phone">
    <svg width="18" height="18" viewBox="0 0 24 24"><circle cx="12" cy="12" r="10" fill="none" stroke="#fff" stroke-width="2"/><path d="M8 7c0 5 4 9 9 9l1-2-3-1-1 1c-2-1-3-2-4-4l1-1-1-3z" fill="#fff"/></svg>
    012-555-0147
  </div>
  <div class="social" style="left:790px;top:4px"></div>
  <div class="social" style="left:830px;top:4px"></div>
  <div class="social" style="left:870px;top:4px"></div>
  <div class="abs sell">
    <svg width="22" height="14" viewBox="0 0 22 14"><path d="M2 9l2-5h12l3 5h1v3H2z" fill="#fff"/><circle cx="6" cy="12" r="2" fill="#6f7b9a"/><circle cx="16" cy="12" r="2" fill="#6f7b9a"/></svg>
    Sell or Buy a Car
  </div>
</header>

<div class="abs logo" style="left:135px;top:82px"><span class="mark"></span>KESTREL BROKERS</div>
<nav class="abs nav"><span class="on">HOME</span><span>SEARCH</span><span>NEW CARS</span><span>OLD CARS</span><span>CONTACT US</span></nav>

<section class="abs hero" role="img" aria-label="Three electric cars parked in front of misty mountain ridges">
  <h1>Australia’s Leading Car Broker<br>Since 2003</h1>
</section>

<section class="abs search">
  <div class="bar">SELECT TYPE OF VEHICLE SEARCH
    <div class="tabs"><span class="on">NEW</span><span>USED</span><span>DEMO</span></div>
  </div>
  <div class="label" style="left:22px;top:77px">SEARCH BY VEHICLE</div>
  <div class="abs" style="left:545px;top:74px;font-size:13px">Select an option below to refine search or</div>
  <div class="abs" style="left:844px;top:72px;width:70px;height:22px;background:var(--brand);color:#fff;font-size:11px;display:flex;align-items:center;justify-content:center">VIEW ALL</div>
  <div class="select" style="left:23px">Location</div>
  <div class="select" style="left:256px">Make</div>
  <div class="select" style="left:489px">Model</div>
  <div class="btn" style="left:723px;top:128px;width:191px;height:36px">Search Vehicle</div>
  <div class="label" style="left:22px;top:202px">SEARCH BY BODY TYPE</div>
  <div class="types">
    <div class="type" style="left:1px"><svg width="54" height="22" viewBox="0 0 54 22"><path d="M4 14l6-6h20l8 5 10 1v4H4z" fill="#444"/><circle cx="14" cy="18" r="3.5" fill="#444" stroke="#fff"/><circle cx="40" cy="18" r="3.5" fill="#444" stroke="#fff"/></svg>SEDAN</div>
    <div class="type" style="left:117px"><svg width="54" height="22" viewBox="0 0 54 22"><path d="M4 16V8l5-5h24l6 6h10v7z" fill="#444"/><circle cx="14" cy="18" r="3.5" fill="#444" stroke="#fff"/><circle cx="40" cy="18" r="3.5" fill="#444" stroke="#fff"/></svg>SUV</div>
    <div class="type" style="left:234px"><svg width="54" height="22" viewBox="0 0 54 22"><path d="M4 15l8-6h16l10 5h10v3H4z" fill="#444"/><circle cx="14" cy="18" r="3.5" fill="#444" stroke="#fff"/><circle cx="40" cy="18" r="3.5" fill="#444" stroke="#fff"/></svg>COUPE</div>
    <div class="type" style="left:351px"><svg width="54" height="22" viewBox="0 0 54 22"><path d="M6 15l6-8h18l8 6h8v4H6z" fill="#444"/><circle cx="15" cy="18" r="3.5" fill="#444" stroke="#fff"/><circle cx="39" cy="18" r="3.5" fill="#444" stroke="#fff"/></svg>COMPACT</div>
    <div class="type" style="left:461px"><svg width="54" height="22" viewBox="0 0 54 22"><path d="M4 16V4h32l8 7h6v5z" fill="#444"/><circle cx="14" cy="18" r="3.5" fill="#444" stroke="#fff"/><circle cx="40" cy="18" r="3.5" fill="#444" stroke="#fff"/></svg>VAN</div>
    <div class="type" style="left:571px"><svg width="54" height="22" viewBox="0 0 54 22"><path d="M4 16V6l4-3h28l8 7h6v6z" fill="#444"/><circle cx="14" cy="18" r="3.5" fill="#444" stroke="#fff"/><circle cx="40" cy="18" r="3.5" fill="#444" stroke="#fff"/></svg>MINIVAN</div>
    <div class="type" style="left:688px"><svg width="54" height="22" viewBox="0 0 54 22"><path d="M2 15V9l6-4h22l6 5h14v5z" fill="#444"/><circle cx="13" cy="18" r="3.5" fill="#444" stroke="#fff"/><circle cx="40" cy="18" r="3.5" fill="#444" stroke="#fff"/></svg>WAGON</div>
    <div class="type" style="left:813px"><svg width="54" height="22" viewBox="0 0 54 22"><path d="M4 15l4-5h10l6-4 4 4h12l10 4v3H4z" fill="#444"/><circle cx="14" cy="18" r="3.5" fill="#444" stroke="#fff"/><circle cx="40" cy="18" r="3.5" fill="#444" stroke="#fff"/></svg>CONVERTIBLE</div>
  </div>
</section>

<h2 class="heading" style="top:910px">ABOUT KESTREL BROKERS</h2>
<div class="photo about-photo" role="img" aria-label="A delighted young man holding up new car keys outdoors"></div>
<div class="abs about-text">
  <p>Lorem ipsum dolor sit amet, consectetuer adcing elit, sed diam nonummy nibh euismod tincidunt ut lareet dre magna aliquam erat volutpat. Ut wisi enim ad minim veniam, sis nostrud exerci tation ullamcorper.</p>
  <p style="margin-top:8px">Lorem ipsum dolor sit amet, consectetuer adcing elit, sed diam nonummy nibh euismod tincidunt ut.</p>
  <h3>We can arrange the following for you:</h3>
  <ul>
    <li><svg width="16" height="16" viewBox="0 0 16 16"><circle cx="8" cy="8" r="6.5" fill="none" stroke="#7f8bab"/><path d="M5 8l2 2 5-5" fill="none" stroke="#7f8bab" stroke-width="1.5"/></svg>Lorem ipsum dolor sit amet, consectetuer</li>
    <li><svg width="16" height="16" viewBox="0 0 16 16"><circle cx="8" cy="8" r="6.5" fill="none" stroke="#7f8bab"/><path d="M5 8l2 2 5-5" fill="none" stroke="#7f8bab" stroke-width="1.5"/></svg>Lorem ipsum dolor sit amet</li>
    <li><svg width="16" height="16" viewBox="0 0 16 16"><circle cx="8" cy="8" r="6.5" fill="none" stroke="#7f8bab"/><path d="M5 8l2 2 5-5" fill="none" stroke="#7f8bab" stroke-width="1.5"/></svg>Lorem ipsum dolor sit amet, consectetuer</li>
    <li><svg width="16" height="16" viewBox="0 0 16 16"><circle cx="8" cy="8" r="6.5" fill="none" stroke="#7f8bab"/><path d="M5 8l2 2 5-5" fill="none" stroke="#7f8bab" stroke-width="1.5"/></svg>Lorem ipsum dolor sit amet, consectetuer</li>
  </ul>
</div>
<div class="btn" style="left:592px;top:1366px;width:161px;height:34px">Contact Us Today</div>

<h2 class="heading" style="top:1532px">POPULAR CARS</h2>
<div class="abs brands">
  <div class="on">MARLOW <span style="position:absolute;right:24px">›</span></div>
  <div>KENJI</div><div>TAVORA</div><div>BERGMANN</div><div>FALCONI</div><div>ARDEN</div>
</div>
<div class="card" style="left:358px"><div class="img" role="img" aria-label="Yellow sports coupe on a desert road" style="background:linear-gradient(180deg,#c99a78,#8f7058 50%,#3b3a3a)"></div><h4>Comet</h4><p>Automatic, Petrol, 10.7 kmpl</p><div class="price"><span>$ 1,800.00</span><i><svg width="12" height="11" viewBox="0 0 12 11"><path d="M6 10L1 5a3 3 0 015-3 3 3 0 015 3z" fill="#fff"/></svg></i></div><span class="get">Get On Road Price</span></div>
<div class="card" style="left:600px"><div class="img" role="img" aria-label="Yellow convertible sports car under trees" style="background:linear-gradient(160deg,#2f6a8a,#d8c23a 55%,#5a5a45)"></div><h4>Vireo</h4><p>Automatic, Petrol, 10.7 kmpl</p><div class="price"><span>$ 1,800.00</span><i><svg width="12" height="11" viewBox="0 0 12 11"><path d="M6 10L1 5a3 3 0 015-3 3 3 0 015 3z" fill="#fff"/></svg></i></div><span class="get">Get On Road Price</span></div>
<div class="card" style="left:840px"><div class="img" role="img" aria-label="Dark sedan parked before a city skyline" style="background:linear-gradient(180deg,#b9c0c9,#8a9099 45%,#2a2c33)"></div><h4>Marlow Sable</h4><p>Automatic, Petrol, 10.7 kmpl</p><div class="price" style="margin-top:2px"><span>$ 1,800.00</span><i><svg width="12" height="11" viewBox="0 0 12 11"><path d="M6 10L1 5a3 3 0 015-3 3 3 0 015 3z" fill="#fff"/></svg></i></div><span class="get" style="margin-top:10px">Get On Road Price</span></div>

<div class="abs band"></div>
<h2 class="heading" style="top:2058px;color:#fff">READ WHAT OUR CUSTOMERS ARE SAYING</h2>
<svg class="arrow" style="left:96px" width="18" height="46" viewBox="0 0 18 46"><path d="M16 2L2 23l14 21" fill="none" stroke="#8a90a0" stroke-width="1.5"/></svg>
<svg class="arrow" style="left:1084px" width="18" height="46" viewBox="0 0 18 46"><path d="M2 2l14 21L2 44" fill="none" stroke="#8a90a0" stroke-width="1.5"/></svg>
<div class="quote" style="left:132px"><h5><b>“</b>Very helpful</h5><p>Lorem ipsum dolor sit amensectetuer adcing elit, sed diam nonummy nibh euismod tincidunt ut lareet.</p><div class="name">Lorem Ispum</div><div class="stars">★★★★☆</div></div>
<div class="quote" style="left:449px"><h5><b>“</b>Excellent service!!!!!</h5><p>Lorem ipsum dolor sit amensectetuer adcing elit, sed diam nonummy nibh euismod tincidunt ut lareet.</p><div class="name">Lorem Ispum</div><div class="stars">★★★★☆</div></div>
<div class="quote" style="left:767px"><h5><b>“</b>Prompt and easy process</h5><p>Lorem ipsum dolor sit amensectetuer adcing elit, sed diam nonummy nibh euismod tincidunt ut lareet.</p><div class="name">Lorem Ispum</div><div class="stars">★★★★☆</div></div>

<section class="products">
  <h2 class="heading" style="top:2442px">OTHER PRODUCTS</h2>
  <p>Lorem ipsum dolor sit amet, consectetuer adcing elit, sed diam nonummy nibh euismod tincidunt ut lareet dre magna aliquam erat volutpat. Ut wisi enim ad minim veniam, sis nostrud exerci tation ullamcorper.</p>
  <div class="prod" style="left:184px"><div class="box"><svg width="64" height="56" viewBox="0 0 64 56"><circle cx="42" cy="14" r="12" fill="#4f5b7a"/><text x="42" y="19" fill="#fff" font-size="14" font-family="Montserrat,sans-serif" text-anchor="middle">£</text><path d="M6 44V34l6-8h30l6 8v10z" fill="#4f5b7a"/><circle cx="16" cy="46" r="5" fill="#4f5b7a" stroke="#fff" stroke-width="2"/><circle cx="40" cy="46" r="5" fill="#4f5b7a" stroke="#fff" stroke-width="2"/></svg></div>Competitive Car<br>Finance</div>
  <div class="prod" style="left:408px"><div class="box"><svg width="70" height="50" viewBox="0 0 70 50"><path d="M4 38V30l5-7h20l5 7v8z" fill="none" stroke="#4f5b7a" stroke-width="2.5"/><circle cx="12" cy="39" r="4" fill="#4f5b7a"/><circle cx="27" cy="39" r="4" fill="#4f5b7a"/><rect x="40" y="6" width="24" height="34" fill="none" stroke="#4f5b7a" stroke-width="2.5"/><path d="M45 15h14M45 22h14M45 29h14" stroke="#4f5b7a" stroke-width="2"/></svg></div>Extended warranty</div>
  <div class="prod" style="left:639px"><div class="box"><svg width="56" height="56" viewBox="0 0 56 56"><path d="M10 20h22l10-6v14l-10-4H26v8h-6l-4 18h-6l4-18H10z" fill="#4f5b7a"/><rect x="30" y="6" width="10" height="8" fill="#4f5b7a"/></svg></div>Point Protection</div>
  <div class="prod" style="left:867px"><div class="box"><svg width="60" height="56" viewBox="0 0 60 56"><path d="M20 18l4-8h12l4 8v8H20z" fill="none" stroke="#4f5b7a" stroke-width="2.5"/><path d="M6 18c0 14 8 24 18 28M54 18c0 14-8 24-18 28" fill="none" stroke="#4f5b7a" stroke-width="3"/></svg></div>Cut the cost not<br>the cover</div>
</section>
<div class="btn" style="left:517px;top:2770px;width:165px;height:35px">Contact Us Today</div>

<h2 class="heading" style="top:2942px">FREQUENTLY ASKED QUESTIONS</h2>
<div class="faq" style="top:3017px;height:38px">Lorem ipsum dolor sit amet, consectetuer<svg width="14" height="12" viewBox="0 0 14 12"><path d="M1 6h11M7 1l5 5-5 5" fill="none" stroke="#666" stroke-width="2"/></svg></div>
<div class="faq" style="top:3069px;height:38px">Lorem ipsum dolor sit amet, consectetuer Lorem ipsum dolor sit amet, consectetuer<svg width="14" height="12" viewBox="0 0 14 12"><path d="M1 6h11M7 1l5 5-5 5" fill="none" stroke="#666" stroke-width="2"/></svg></div>
<div class="faq" style="top:3121px;height:38px">Lorem ipsum dolor sit amet, consectetuer<svg width="14" height="12" viewBox="0 0 14 12"><path d="M1 6h11M7 1l5 5-5 5" fill="none" stroke="#666" stroke-width="2"/></svg></div>
<div class="faq" style="top:3174px;height:38px">Lorem ipsum dolor sit amet, consectetuer Lorem ipsum dolor sit amet, consectetuer<svg width="14" height="12" viewBox="0 0 14 12"><path d="M1 6h11M7 1l5 5-5 5" fill="none" stroke="#666" stroke-width="2"/></svg></div>
<div class="faq" style="top:3226px;height:107px">Lorem ipsum dolor sit amet, consectetuer lorem isumy<svg width="12" height="14" viewBox="0 0 12 14"><path d="M6 1v11M1 7l5 5 5-5" fill="none" stroke="#2a9d8f" stroke-width="2"/></svg><p>Lorem ipsum dolor sit amet, consectetuer adipiscing elit, sed diam nonummy nibh euismod tincidunt ut laoreet dolore magna aliquam erat volutpat. Ut wisi enim ad minim veniam.</p></div>
<div class="btn" style="left:510px;top:3345px;width:98px;height:35px">View All</div>

<footer class="abs footer" role="img" aria-label="Harbour city skyline at dusk under a blue tint"></footer>
<div class="abs logo" style="left:0;width:1200px;justify-content:center;top:3575px;color:#fff;font-size:22px"><span class="mark" style="background:#fff;width:22px;height:22px"></span>KESTREL BROKERS</div>
<div class="social" style="left:546px;top:3650px;background:#6f7b9a"></div>
<div class="social" style="left:585px;top:3650px;background:#6f7b9a"></div>
<div class="social" style="left:624px;top:3650px;background:#6f7b9a"></div>
<nav class="abs fnav"><span>HOME</span><span>SEARCH</span><span>NEW CARS</span><span>OLD CARS</span><span>CONTACT US</span></nav>
<div class="btn" style="left:449px;top:3746px;width:302px;height:52px;background:#7f8bab;font-size:17px">Save Thousands on New Car Now</div>
<div class="abs copy">Copyright © 2019 Kestrel Brokers. All Rights Reserved. Terms of Use | Privacy Policy</div>

</body>
</html>
```